Letterhead for Law Firm - Logo already prepared

I previously used to prepare a logo which I was quite pleased with, a copy is attached for your reference. I would like the font of the logo to be all the same size, rather than the 'S' and 'L' being larger than the other letters.
I have copies of the attached in other formats if necessary.
I need a letterhead prepared which is virtually identical to the draft attached, however I will be adding an address, phone number, fax number, mobile number and email. I will provide these details with whoever can assist me.
I will also be providing insurance details to be listed at the foot of the page.
Finally, I need the file to be supplied as a high resolution pdf with 2mm bleed.
If you require any further information, please do not hesitate to contact me.

```html
<!DOCTYPE html>
<html lang="en">
<head>
<meta charset="utf-8">
<title>Vantrell Legal — Letterhead</title>
<link rel="stylesheet" href="https://fonts.googleapis.com/css2?family=Arimo:wght@400;700&family=Cousine&display=swap">
<style>
  :root {
    --brand-orange: #f58220;
    --ink-dark: #333333;
    --ink-muted: #444444;
    --rule-grey: #5a5a5a;
    --paper: #ffffff;
  }
  html, body {
    margin: 0;
    padding: 0;
    overflow: hidden;
    background: var(--paper);
  }
  .letterhead {
    position: relative;
    width: 874px;
    height: 1200px;
    background: var(--paper);
    overflow: hidden;
    font-family: "Arimo", Arial, sans-serif;
  }
  .brand-mark {
    position: absolute;
    top: 1px;
    left: 320px;
    display: flex;
    align-items: center;
    gap: 8px;
  }
  .brand-mark__dot {
    width: 66px;
    height: 66px;
    border-radius: 50%;
    background: var(--brand-orange);
  }
  .brand-mark__name {
    font-family: "Arimo", Arial, sans-serif;
    font-weight: 400;
    font-size: 28px;
    color: var(--ink-dark);
    letter-spacing: -0.3px;
  }
  .title-band {
    position: absolute;
    top: 93px;
    left: 0;
    width: 582px;
    height: 101px;
    background: var(--brand-orange);
    display: flex;
    align-items: center;
    justify-content: center;
  }
  .title-band__name {
    margin: 0;
    font-family: "Arimo", Arial, sans-serif;
    font-weight: 700;
    font-size: 58px;
    color: var(--paper);
    letter-spacing: 1px;
    padding-left: 40px;
  }
  .contact-divider {
    position: absolute;
    top: 93px;
    left: 598px;
    width: 2px;
    height: 101px;
    background: var(--brand-orange);
  }
  .contact-list {
    position: absolute;
    top: 106px;
    left: 608px;
    margin: 0;
    padding: 0;
    list-style: none;
    font-size: 16px;
    line-height: 21.5px;
    color: var(--ink-dark);
  }
  .contact-list__phone {
    font-family: "Cousine", "Courier New", monospace;
  }
  .footer-label {
    position: absolute;
    top: 1171px;
    left: 17px;
    margin: 0;
    font-size: 16px;
    color: var(--ink-muted);
    word-spacing: 4px;
  }
  .footer-rule {
    position: absolute;
    top: 1195px;
    left: 20px;
    width: 840px;
    height: 2px;
    background: var(--rule-grey);
  }
</style>
</head>
<body>
<div class="letterhead">
  <div class="brand-mark">
    <span class="brand-mark__dot"></span>
    <span class="brand-mark__name">Vantrell Legal</span>
  </div>

  <header class="title-band">
    <h1 class="title-band__name">Vantrell Legal</h1>
  </header>
  <div class="contact-divider"></div>
  <ul class="contact-list">
    <li class="contact-list__phone">Tel:98-5120-3377</li>
    <li>www.vantrelllegal.com</li>
    <li>facebook/pages/vantrelllegal</li>
  </ul>

  <p class="footer-label">Insurance details:</p>
  <div class="footer-rule"></div>
</div>
</body>
</html>
```